Modern Medical Optometry Website

We need mordern, Patient friendly website. Easy to navigate and enhance our advance medical technology and excellent patient care.
1. HOME PAGE
2. OUR TEAM PAGE
3. EYECARE PAGE - VISION SERVICES, EYE EXAMS, KERATOCONUS CENTER, GLAUCOMA , DIABITES, VELMORIN EXAM, DIGITAL RETINAL, OCT.
4. MYOPIA CONTROL CLINIC
5. DRY EYE CLINIC
6. EYEWEAR
7. PATIENT CENTER - BLOG
7. CONTACT US
This is our current website www.lumvarta.com
and We want to add more content and a cleaner design like these website
http://norvellbrookclinic.com/
https://www.tqvamori.com/

```html
<!DOCTYPE html>
<html lang="en">
<head>
<meta charset="utf-8">
<title>Lumvarta Optometry</title>
<link href="https://fonts.googleapis.com/css2?family=Montserrat:wght@400;600;700;800&family=Open+Sans:wght@400;600&display=swap" rel="stylesheet">
<style>
:root{
  --yellow:#f8c82d;
  --footer:#fbd03a;
  --ink:#1f1f24;
  --text:#4a4a50;
  --muted:#8a8a90;
  --hero:#7d7993;
  --soft:#f1efef;
  --white:#ffffff;
}
*{margin:0;padding:0;box-sizing:border-box}
html,body{width:1200px;height:4932px;overflow:hidden;background:var(--white)}
body{font-family:"Open Sans",Arial,sans-serif;color:var(--text);position:relative}
.abs{position:absolute}
.section{position:absolute;left:0;width:1200px}
.heading{font-family:"Montserrat",Arial,sans-serif;font-weight:800;color:var(--ink);letter-spacing:2px}
.section-title{position:absolute;left:0;width:1200px;text-align:center;font-size:40px}
.section-title::after{content:"";display:block;width:44px;height:3px;background:var(--muted);margin:18px auto 0}
.btn{position:absolute;background:var(--yellow);color:var(--ink);font-family:"Montserrat",Arial,sans-serif;font-weight:700;font-size:15px;letter-spacing:1px;display:flex;align-items:center;justify-content:center}
.photo{position:absolute}
.para{position:absolute;font-size:15.5px;line-height:24px;color:var(--text)}

/* hero */
.hero{top:0;height:707px;background:var(--hero)}
.hero-photo{left:540px;top:0;width:660px;height:707px;background:linear-gradient(160deg,#9a8f9e 0%,#c79a7a 40%,#a0525a 75%,#6e6b88 100%)}
.brand{left:36px;top:34px;display:flex;align-items:center;gap:12px}
.brand-mark{width:22px;height:22px;background:var(--yellow)}
.brand-name{font-family:"Montserrat",Arial,sans-serif;font-weight:700;font-size:22px;color:var(--yellow);letter-spacing:1px;line-height:26px}
.top-phone{left:845px;top:22px;width:125px;height:28px;border:1px solid var(--white);color:var(--white);font-size:13px;font-weight:600;display:flex;align-items:center;justify-content:center;gap:6px}
.top-cta{left:980px;top:22px;width:192px;height:28px;font-size:12px}
.main-nav{left:340px;top:72px;width:832px;display:flex;justify-content:space-between;font-family:"Montserrat",Arial,sans-serif;font-weight:700;font-size:12.5px;color:var(--white);letter-spacing:.3px}
.hero-welcome{left:78px;top:328px;color:var(--white);font-size:29px;letter-spacing:2px}
.hero-name{left:78px;top:366px;color:var(--white);font-size:42px;letter-spacing:2px}
.hero-btn{left:80px;top:448px;width:145px;height:38px}
.dots{position:absolute;display:flex;gap:8px}
.dots span{width:11px;height:11px;border-radius:50%;background:var(--white)}
.dots span.on{background:var(--yellow)}

/* eyecare */
.eyecare{top:707px;height:658px}
.service-card{position:absolute;top:171px;width:376px;height:372px}
.service-photo{left:0;top:0;width:376px;height:322px}
.service-label{position:absolute;left:14px;top:334px;font-family:"Montserrat",Arial,sans-serif;font-size:19px;color:var(--ink)}
.service-label b{font-weight:800}
.service-more{position:absolute;right:8px;top:300px;width:50px;height:64px;background:var(--yellow);color:var(--white);font-family:"Montserrat",Arial,sans-serif;font-size:9px;font-weight:700;display:flex;flex-direction:column;align-items:center;justify-content:center;gap:4px}
.dots.small span{width:8px;height:8px;background:#cfcfd2}
.dots.small span.on{background:var(--yellow)}

/* feature blocks */
.myopia{top:1365px;height:668px;background:var(--white)}
.dry-eye{top:2033px;height:625px;background:var(--soft)}
.frame{position:absolute;border:8px solid var(--yellow)}
.feature-title{position:absolute;font-size:40px;line-height:48px;letter-spacing:2px}
.feature-title::after{content:"";display:block;width:40px;height:3px;background:var(--muted);margin-top:14px}
.feature-btn{width:146px;height:40px}

/* testimonials */
.testimonials{top:2658px;height:625px}
.quote-card{position:absolute;top:204px;width:452px;height:330px;background:var(--soft)}
.quote-card .line-top{position:absolute;right:-8px;top:-8px;width:300px;height:8px;background:var(--yellow)}
.quote-card .line-side{position:absolute;right:-8px;top:-8px;width:8px;height:80px;background:var(--yellow)}
.quote-card .line-bottom{position:absolute;left:-8px;bottom:-8px;width:300px;height:8px;background:var(--yellow)}
.quote-card .line-left{position:absolute;left:-8px;bottom:-8px;width:8px;height:80px;background:var(--yellow)}
.quote-mark{position:absolute;left:40px;top:24px;font-family:"Montserrat",Arial,sans-serif;font-weight:800;font-size:46px;color:var(--yellow);line-height:1}
.quote-text{position:absolute;left:72px;top:40px;width:330px;font-size:15px;line-height:23px;color:var(--text)}
.quote-author{position:absolute;left:72px;top:250px;display:flex;align-items:center;gap:14px}
.avatar{width:30px;height:30px;border-radius:50%;background:#b7b2ad}
.author-sep{width:1px;height:34px;background:#cfcfcf}
.author-name{font-family:"Montserrat",Arial,sans-serif;font-weight:700;font-size:11px;color:var(--ink);letter-spacing:.5px}
.stars{color:var(--yellow);font-size:13px;letter-spacing:2px}
.slider-arrow{position:absolute;top:2992px;width:38px;height:38px;border-radius:50%;border:1px solid #9a9aa0;background:var(--white);display:flex;align-items:center;justify-content:center}

/* blog */
.blog{top:3283px;height:675px;background:var(--soft)}
.blog-card{position:absolute;top:165px;width:292px;height:444px;background:var(--white);box-shadow:0 2px 8px rgba(0,0,0,.08)}
.blog-photo{left:0;top:0;width:292px;height:262px}
.blog-date{position:absolute;left:22px;top:250px;background:var(--white);font-size:10px;padding:3px 8px;color:var(--text)}
.blog-title{position:absolute;left:28px;top:290px;font-family:"Montserrat",Arial,sans-serif;font-weight:700;font-size:18px;color:var(--ink)}
.blog-text{position:absolute;left:28px;top:324px;width:240px;font-size:12px;line-height:17px;color:var(--text)}
.blog-btn{left:28px;top:388px;width:100px;height:28px;font-size:11px}

/* map */
.map{top:3958px;height:542px;background:linear-gradient(135deg,#d9dcd6 0%,#c9d9b9 40%,#e2e2dd 70%,#bfd3ac 100%)}
.address-card{position:absolute;background:var(--white);display:flex;align-items:center;gap:12px;padding:10px 14px;font-size:12px;line-height:17px;color:var(--text);box-shadow:0 1px 4px rgba(0,0,0,.2)}
.address-mark{width:20px;height:20px;background:var(--yellow);flex:none}

/* footer */
.footer{top:4500px;height:432px;background:var(--footer)}
.footer-brand{left:0;top:80px;width:1200px;display:flex;flex-direction:column;align-items:center;gap:14px}
.footer-brand .brand-mark{width:40px;height:40px;background:var(--white)}
.footer-brand .brand-name{color:var(--white);font-size:26px}
.footer-rule{position:absolute;left:195px;width:810px;height:1px;background:rgba(255,255,255,.8)}
.footer-nav{left:0;top:244px;width:1200px;display:flex;justify-content:center;gap:12px;font-family:"Montserrat",Arial,sans-serif;font-weight:700;font-size:12.5px;color:var(--ink)}
.footer-nav i{font-style:normal;color:var(--ink)}
.socials{left:0;top:330px;width:1200px;display:flex;justify-content:center;gap:10px}
.socials span{width:22px;height:22px;border-radius:50%}
.copyright{left:0;top:386px;width:1200px;text-align:center;font-size:12px;color:var(--ink)}
</style>
</head>
<body>

<section class="section hero">
  <div class="photo hero-photo" role="img" aria-label="Smiling young woman in a hat adjusting her glasses"></div>
  <div class="abs brand"><span class="brand-mark"></span><span class="brand-name">LUMVARTA<br>OPTOMETRY</span></div>
  <div class="abs top-phone">
    <svg width="12" height="12" viewBox="0 0 24 24"><path fill="#fff" d="M6.6 10.8a15 15 0 006.6 6.6l2.2-2.2c.3-.3.7-.4 1-.2 1.1.4 2.3.6 3.6.6.6 0 1 .4 1 1V20c0 .6-.4 1-1 1A17 17 0 013 4c0-.6.4-1 1-1h3.5c.6 0 1 .4 1 1 0 1.3.2 2.5.6 3.6.1.3 0 .7-.2 1z"/></svg>
    555 204 7180
  </div>
  <div class="btn top-cta">MAKE AN APPOINTMENT</div>
  <nav class="abs main-nav">
    <span>HOME</span><span>OUR TEAM</span><span>EYECARE</span><span>MYOPIA CONTROL CLINIC</span><span>DRY EYE CLINIC</span><span>EYEWEAR</span><span>PATIENT CENTER</span><span>CONTACT</span>
  </nav>
  <h2 class="abs heading hero-welcome">WELCOME TO</h2>
  <h1 class="abs heading hero-name">LUMVARTA OPTOMETRY</h1>
  <div class="btn hero-btn">READ MORE</div>
  <div class="dots" style="left:90px;top:612px"><span></span><span></span><span class="on"></span><span></span><span></span></div>
</section>

<section class="section eyecare">
  <h2 class="heading section-title" style="top:58px">EYECARE</h2>
  <div class="service-card" style="left:26px">
    <div class="photo service-photo" role="img" aria-label="Optometrist examining a patient with a phoropter" style="background:linear-gradient(135deg,#d9d9dc,#8e9399 60%,#5a5f66)"></div>
    <div class="service-label"><b>VISION</b> SERVICES</div>
    <div class="service-more"><svg width="14" height="18" viewBox="0 0 14 18"><path d="M3 2l8 7-8 7" stroke="#fff" stroke-width="2.5" fill="none"/></svg>MORE</div>
  </div>
  <div class="service-card" style="left:414px">
    <div class="photo service-photo" role="img" aria-label="Patient reading an eye chart during an eye test" style="background:linear-gradient(135deg,#eceae6,#b5aea6 55%,#6b6660)"></div>
    <div class="service-label"><b>VISION</b> SERVICES</div>
    <div class="service-more"><svg width="14" height="18" viewBox="0 0 14 18"><path d="M3 2l8 7-8 7" stroke="#fff" stroke-width="2.5" fill="none"/></svg>MORE</div>
  </div>
  <div class="service-card" style="left:802px">
    <div class="photo service-photo" role="img" aria-label="Close-up of a green eye" style="background:radial-gradient(circle at 45% 50%,#c9b26a,#7c8a4a 35%,#9c5a3a 70%,#5a3325)"></div>
    <div class="service-label"><b>GLAUCOMA</b></div>
    <div class="service-more"><svg width="14" height="18" viewBox="0 0 14 18"><path d="M3 2l8 7-8 7" stroke="#fff" stroke-width="2.5" fill="none"/></svg>MORE</div>
  </div>
  <div class="dots small" style="left:566px;top:598px"><span class="on"></span><span></span><span></span><span></span><span></span></div>
</section>

<section class="section myopia">
  <div class="frame" style="left:158px;top:70px;width:438px;height:500px"></div>
  <div class="photo" role="img" aria-label="Eye imaging device screen showing a scanned eye" style="left:138px;top:84px;width:440px;height:496px;background:linear-gradient(135deg,#6f6a5c,#c9c6b6 45%,#8a8770 75%,#3c3a33)"></div>
  <h2 class="heading feature-title" style="left:665px;top:112px">MYOPIA CONTROL<br>CLINIC</h2>
  <p class="para" style="left:665px;top:244px;width:400px">Sed ut perspiciatis unde omnis iste natus error sit voluptatem accusantium doloremque laudantium, totam rem aperiam, eaque ipsa quae ab illo inventore veritatis et quasi architecto beatae vitae dicta sunt explicabo. Nemo enim ipsam.</p>
  <p class="para" style="left:665px;top:378px;width:400px">But I must explain to you how all this mistaken idea of denouncing pleasure and praising pain was born and I will give you a complete account of the system, and expound the actual teaching.</p>
  <div class="btn feature-btn" style="left:665px;top:500px">READ MORE</div>
</section>

<section class="section dry-eye">
  <div class="frame" style="left:598px;top:52px;width:450px;height:506px"></div>
  <div class="photo" role="img" aria-label="Close-up of an eye with pink-red tones and blue light" style="left:612px;top:68px;width:430px;height:500px;background:linear-gradient(150deg,#cfe6f1 0%,#8fb6cf 30%,#6a5f8a 55%,#b0446e 70%,#3a5b82 100%)"></div>
  <h2 class="heading feature-title" style="left:141px;top:104px">DRY EYE CLINIC</h2>
  <p class="para" style="left:141px;top:200px;width:400px">Sed ut perspiciatis unde omnis iste natus error sit voluptatem accusantium doloremque laudantium, totam rem aperiam, eaque ipsa quae ab illo inventore veritatis et quasi architecto beatae vitae dicta sunt explicabo. Nemo enim ipsam.</p>
  <p class="para" style="left:141px;top:332px;width:400px">But I must explain to you how all this mistaken idea of denouncing pleasure and praising pain was born and I will give you a complete account of the system, and expound the actual teaching.</p>
  <div class="btn feature-btn" style="left:141px;top:456px">READ MORE</div>
</section>

<section class="section testimonials">
  <h2 class="heading section-title" style="top:72px">TESTIMONIALS</h2>
  <div class="quote-card" style="left:134px">
    <span class="line-top"></span><span class="line-side"></span><span class="line-bottom"></span><span class="line-left"></span>
    <div class="quote-mark">“</div>
    <p class="quote-text">Love this place to death! I've been going for a few years and everyone there is so nice and inform patients of their procedures. They are bilingual in Vietnamese and English which is awesome. Not to mention all the staff are pretty nice and kind! Shoutout to Dr. Osk and Dr. Pell. Of course to Tavi too!</p>
    <div class="quote-author"><span class="avatar"></span><span class="author-sep"></span><div><div class="author-name">MARLO VEEN</div><div class="stars">★★★★★</div></div></div>
  </div>
  <div class="quote-card" style="left:622px">
    <span class="line-top"></span><span class="line-side"></span><span class="line-bottom"></span><span class="line-left"></span>
    <div class="quote-mark">“</div>
    <p class="quote-text">I really love this place and the people who work there. They are so very helpful and very nice. You should go and check it out and you will see for yourself how nice it is to go there!!!</p>
    <div class="quote-author"><span class="avatar"></span><span class="author-sep"></span><div><div class="author-name">TOBY RENSHAW</div><div class="stars">★★★★★</div></div></div>
  </div>
</section>
<div class="slider-arrow" style="left:54px"><svg width="12" height="14" viewBox="0 0 12 14"><path d="M8 2L3 7l5 5" stroke="#555" stroke-width="2" fill="none"/></svg></div>
<div class="slider-arrow" style="left:1094px"><svg width="12" height="14" viewBox="0 0 12 14"><path d="M4 2l5 5-5 5" stroke="#555" stroke-width="2" fill="none"/></svg></div>

<section class="section blog">
  <h2 class="heading section-title" style="top:58px">LATEST BLOG</h2>
  <article class="blog-card" style="left:145px">
    <div class="photo blog-photo" role="img" aria-label="Man in a blue jacket wearing glasses" style="background:linear-gradient(135deg,#3e7bc4,#8fb8e0 45%,#c79a7a 70%,#2d4f86)"></div>
    <span class="blog-date">16 FEB, 2019</span>
    <h3 class="blog-title">Lorem Ipsum is simply</h3>
    <p class="blog-text">At vero eos et accusamus et iusto odio dignissimos ducimus qui blanditiis praesentium.</p>
    <div class="btn blog-btn">READ MORE</div>
  </article>
  <article class="blog-card" style="left:454px">
    <div class="photo blog-photo" role="img" aria-label="Extreme close-up of a blue iris" style="background:radial-gradient(circle at 50% 45%,#0b0b10 18%,#2a4f78 34%,#6f95b8 52%,#1c2a3a 80%)"></div>
    <span class="blog-date">16 FEB, 2019</span>
    <h3 class="blog-title">Lorem Ipsum is simply</h3>
    <p class="blog-text">At vero eos et accusamus et iusto odio dignissimos ducimus qui blanditiis praesentium.</p>
    <div class="btn blog-btn">READ MORE</div>
  </article>
  <article class="blog-card" style="left:763px">
    <div class="photo blog-photo" role="img" aria-label="Close-up of an eye behind black glasses frames" style="background:linear-gradient(180deg,#f2e6dd,#d8b8a2 45%,#5a3a2a 60%,#e8d4c4)"></div>
    <span class="blog-date">16 FEB, 2019</span>
    <h3 class="blog-title">Lorem Ipsum is simply</h3>
    <p class="blog-text">At vero eos et accusamus et iusto odio dignissimos ducimus qui blanditiis praesentium.</p>
    <div class="btn blog-btn">READ MORE</div>
  </article>
</section>

<section class="section map" role="img" aria-label="Street map of the area around the two clinic locations">
  <div class="address-card" style="left:560px;top:70px"><span class="address-mark"></span><span>2215 Hollin Rd, Suite 4,<br>Marrow Hills, CA 90418<br>Phone: 555-318-6642</span></div>
  <div class="address-card" style="left:368px;top:226px"><span class="address-mark"></span><span>4180 Calloway Ave, Brenmoor, CA 90412<br>Phone: 555-204-7180</span></div>
  <svg class="abs" style="left:670px;top:158px" width="22" height="30" viewBox="0 0 22 30"><path d="M11 0C5 0 0 5 0 11c0 8 11 19 11 19s11-11 11-19C22 5 17 0 11 0z" fill="#d8282b"/><circle cx="11" cy="11" r="4" fill="#fff"/></svg>
  <svg class="abs" style="left:509px;top:312px" width="22" height="30" viewBox="0 0 22 30"><path d="M11 0C5 0 0 5 0 11c0 8 11 19 11 19s11-11 11-19C22 5 17 0 11 0z" fill="#d8282b"/><circle cx="11" cy="11" r="4" fill="#fff"/></svg>
</section>

<footer class="section footer">
  <div class="abs footer-brand"><span class="brand-mark"></span><span class="brand-name">LUMVARTA OPTOMETRY</span></div>
  <div class="footer-rule" style="top:230px"></div>
  <nav class="abs footer-nav">
    <span>HOME</span><i>|</i><span>OUR TEAM</span><i>|</i><span>EYECARE</span><i>|</i><span>MYOPIA CONTROL CLINIC</span><i>|</i><span>DRY EYE CLINIC</span><i>|</i><span>EYEWEAR</span><i>|</i><span>PATIENT CENTER</span><i>|</i><span>CONTACT US</span>
  </nav>
  <div class="footer-rule" style="top:288px"></div>
  <div class="abs socials"><span style="background:#3b5ba0"></span><span style="background:#d5453a"></span><span style="background:#2a6fb0"></span><span style="background:#e0503c"></span></div>
  <p class="abs copyright">Copyright © 2019 All Right Reserved</p>
</footer>

</body>
</html>
```